Add in Hockey Magazine

We are looking for a black and white advertisement size 7.5x5 and 3.75 x10 and full page 7.5x10 inches, for our dental practise. We want to include our dentists names and contact info. We want to incorporate a maple leaf theme ( see attached ) with a fun hockey tooth theme for families. It will run in Greenstripe magazine available to view at www.northfieldpucksters.example
Our web site is www.smilesbythemill.example

Thanks Kat Morrow

Target Market(s)

families

Requirements
Must have
• Dentist names and clinic name address and phone numbers:
• Smiles by the MILL
• Dr. Katrina Morrow D.D.S.
• Dr. Liz Pennock D.D.S.
• Tel 403-555-0148
• fax:403-555-0172
• 204-318 Willow Crest Rd. SE
• Calgary, Alberta
• T5X 9Q7
• www.smilesbythemill.example
Nice to have
• Family dental practise gladly accepting new patients
Should not have
• Can't have any claims about being superior or better than any other office or dentist

```html
<!DOCTYPE html>
<html lang="en">
<head>
<meta charset="utf-8">
<title>Smiles by the Mill – Hockey Magazine Ad</title>
<link rel="stylesheet" href="https://fonts.googleapis.com/css2?family=Alegreya:ital,wght@1,900&family=Libre+Baskerville:wght@400;700&family=Tinos&display=swap">
<style>
  :root {
    --ink: #000000;
    --paper: #ffffff;
    --photo-light: #d9d9d9;
    --photo-dark: #2a2a2a;
    --rule: #bfbfbf;
    --mark: #8a8a8a;
  }
  html, body {
    margin: 0;
    padding: 0;
    width: 1200px;
    height: 3203px;
    overflow: hidden;
    background: var(--paper);
  }
  .ad {
    position: relative;
    width: 1200px;
    height: 3203px;
    background: var(--paper);
    overflow: hidden;
  }
  .hero-photo {
    position: absolute;
    left: 0;
    top: 300px;
    width: 1155px;
    height: 1056px;
    background: radial-gradient(ellipse at 45% 40%, var(--photo-light) 0%, #8c8c8c 45%, var(--photo-dark) 100%);
  }
  .headline {
    position: absolute;
    left: 0;
    right: 0;
    top: 80px;
    margin: 0;
    text-align: center;
    font-family: "Alegreya", Georgia, serif;
    font-style: italic;
    font-weight: 900;
    font-size: 172px;
    line-height: 1;
    letter-spacing: 1px;
    color: var(--ink);
  }
  .info-panel {
    position: absolute;
    left: 0;
    top: 1356px;
    width: 1200px;
    height: 1847px;
    background: var(--ink);
    color: var(--paper);
  }
  .pitch {
    position: absolute;
    left: 0;
    right: 0;
    margin: 0;
    text-align: center;
    font-family: "Libre Baskerville", Georgia, serif;
    font-weight: 700;
    font-size: 52px;
    line-height: 1.15;
    letter-spacing: 1px;
  }
  .pitch--offer { top: 110px; }
  .pitch--call { top: 300px; }
  .brand {
    position: absolute;
    left: 55px;
    top: 470px;
    width: 1100px;
    height: 330px;
  }
  .brand-mark {
    position: absolute;
    left: 20px;
    top: 40px;
    width: 230px;
    height: 230px;
    border-radius: 50%;
    background: var(--mark);
  }
  .brand-name {
    position: absolute;
    left: 370px;
    top: 20px;
    margin: 0;
    font-family: "Tinos", "Times New Roman", serif;
    font-weight: 400;
    font-size: 88px;
    line-height: 1.25;
    color: var(--paper);
  }
  .brand-name .line { display: block; }
  .brand-name .line--indent { padding-left: 240px; }
  .brand-name .line--small { font-size: 46px; padding-left: 160px; line-height: 1.2; }
  .website {
    position: absolute;
    left: 0;
    right: 0;
    top: 830px;
    margin: 0;
    text-align: center;
    font-family: "Libre Baskerville", Georgia, serif;
    font-weight: 700;
    font-size: 56px;
    letter-spacing: 1px;
  }
  .divider {
    position: absolute;
    left: 64px;
    top: 966px;
    width: 1090px;
    height: 3px;
    background: var(--rule);
  }
  .contact {
    position: absolute;
    left: 75px;
    top: 1030px;
    margin: 0;
    padding: 0;
    list-style: none;
    font-family: "Tinos", "Times New Roman", serif;
    font-size: 41px;
    line-height: 1.2;
  }
  .contact li { position: absolute; left: 0; white-space: nowrap; }
  .contact strong { font-family: "Libre Baskerville", Georgia, serif; font-weight: 700; font-size: 38px; }
  .contact .address-line2 { padding-left: 130px; }
</style>
</head>
<body>
  <main class="ad">
    <div class="hero-photo" role="img" aria-label="Black and white photo of a cheering hockey player in helmet and gloves, holding up his stick and grinning with a missing front tooth"></div>
    <h1 class="headline">WE CAN FIX IT!</h1>

    <section class="info-panel">
      <p class="pitch pitch--offer">Family dental practice gladly<br>accepting new patients!</p>
      <p class="pitch pitch--call">So what are you waiting for?</p>

      <div class="brand">
        <div class="brand-mark"></div>
        <p class="brand-name">
          <span class="line">Smiles</span>
          <span class="line line--indent">by the Mill</span>
          <span class="line line--small">on willow crest</span>
        </p>
      </div>

      <p class="website">www.smilesbythemill.example</p>
      <div class="divider"></div>

      <ul class="contact">
        <li style="top:0"><strong>Dr. Liz Pennock,</strong> DDS</li>
        <li style="top:100px"><strong>Dr. Katrina Morrow,</strong> DDS</li>
        <li style="top:210px">Add: <strong>204-318 Willow Crest Rd. SE</strong></li>
        <li style="top:266px" class="address-line2"><strong>Calgary, AB &nbsp; T5X 9Q7</strong></li>
        <li style="top:385px">Email: <strong>Frontdesk@smilesbythemill.example</strong></li>
        <li style="top:490px">Tel: <strong>403-555-0148</strong></li>
        <li style="top:605px">Fax: <strong>403-555-0172</strong></li>
      </ul>
    </section>
  </main>
</body>
</html>
```